Vexor Ridge website

i'm looking for a promotional website for my business.
we provide Rope Access, Work at Height & Difficult Access services.
we treat water leak into buildings, external renovation of buildings, windows cleaning, confined spaces services and practically jobs in which the access is difficult.
here are examples of web site i like :
http://www.pixelbarnwebs.example/site-themes/51827.html
http://www.pixelbarnwebs.example/page-templates/62914.html

Target Market(s)

private people, commercial household chiefs, maintenance managers

Industry/Entity Type

Business

Requirements
Must have
• - mobile friendly
- chatterbay redirection
- 5 tabs
- one more customizable page - so i can add a photo and a description of the service corresponding (for now i offer 7 different services)
- contact us on each page with no redirection
- we are offering 7 different services
the website will be published in Israel which means right to left or centered for english option in the future. (logo on left hand corner)

- no flash
- should be future customisable - for future
Nice to have
• - a space for a slogan
- non scrollable
- photos on the landing page + redirection to gallery (photos and short films)
- 3 dynamic banners with short description of the theme of each, clicking on the banner after it opened will redirect to it's corresponding page.

```html
<!DOCTYPE html>
<html lang="en">
<head>
<meta charset="utf-8">
<title>Vexor Ridge</title>
<link rel="stylesheet" href="https://fonts.googleapis.com/css2?family=Fondamento&family=Noto+Sans:wght@400;700&display=swap">
<style>
  :root {
    --page-bg: #f3f3f3;
    --ink: #111111;
    --label: #4a4a4a;
    --muted: #9a9a9a;
    --nav-bg: #000000;
    --nav-active: #ff0000;
    --nav-text: #ffffff;
    --tab-bg-top: #f1f1f1;
    --tab-bg-mid: #e2e2e2;
    --tab-border: #c9c9c9;
    --tab-title: #4b4b4b;
    --panel-bg: #ffffff;
    --panel-border: #a9a9a9;
    --field-border: #a8a8a8;
    --submit: #27a3cb;
    --submit-border: #1d7f9f;
    --social-a: #3b5998;
    --social-b: #d8492f;
    --social-c: #37b2e3;
  }
  * { box-sizing: border-box; margin: 0; padding: 0; }
  html, body { width: 1200px; height: 750px; overflow: hidden; }
  body {
    background: var(--page-bg);
    font-family: "Noto Sans", Verdana, sans-serif;
    color: var(--ink);
    position: relative;
  }
  .site { position: absolute; left: 120px; top: 0; width: 960px; height: 750px; }

  .brand {
    position: absolute; left: 6px; top: 34px;
    display: flex; align-items: center; gap: 10px;
    font-family: "Noto Sans", Verdana, sans-serif;
    font-weight: 700; font-size: 26px; color: var(--ink);
  }
  .brand-mark { width: 18px; height: 18px; border-radius: 50%; background: var(--ink); }

  .main-nav {
    position: absolute; right: 0; top: 0; height: 36px;
    background: var(--nav-bg); display: flex; align-items: flex-start;
  }
  .main-nav a {
    color: var(--nav-text); text-decoration: none; font-size: 16px;
    height: 36px; line-height: 36px; padding: 0 11px;
  }
  .main-nav a.is-active {
    background: var(--nav-active); height: 45px; width: 77px;
    text-align: center; padding: 0;
  }

  .social {
    position: absolute; right: 6px; top: 54px;
    display: flex; gap: 10px; font-size: 12px; color: var(--label);
  }
  .social span { display: flex; align-items: center; gap: 4px; }
  .social i { display: block; width: 12px; height: 12px; border-radius: 2px; }

  .tab {
    position: absolute; left: 0; width: 960px;
    border: 1px solid var(--tab-border); border-radius: 3px;
    background: linear-gradient(var(--tab-bg-top), var(--tab-bg-top) 40%, var(--tab-bg-mid) 55%, var(--tab-bg-top) 75%);
  }
  .tab-head {
    height: 44px; display: flex; align-items: center;
    font-family: "Fondamento", cursive; font-size: 22px; color: var(--tab-title);
    padding-left: 15px;
  }
  .tab-head svg { margin-right: 16px; }
  .tab.is-open { background: var(--panel-bg); border-color: var(--panel-border); }
  .tab.is-open .tab-head { color: var(--ink); height: 43px; border-bottom: 1px solid var(--panel-border); }

  .contact-form { position: relative; height: 287px; }
  .field-label { position: absolute; left: 46px; font-size: 15px; color: var(--label); }
  .field {
    position: absolute; left: 219px; width: 697px; height: 43px;
    border: 1px solid var(--field-border); background: #fff;
    font-family: inherit; font-size: 17px; color: var(--muted);
    padding: 0 10px; line-height: 41px;
  }
  .field.is-area { height: 103px; width: 695px; }
  .submit {
    position: absolute; left: 805px; top: 229px; width: 107px; height: 38px;
    background: var(--submit); border: 1px solid var(--submit-border); border-radius: 2px;
    color: #fff; font-family: inherit; font-weight: 700; font-size: 17px;
  }

  .site-footer {
    position: absolute; right: 6px; top: 617px; font-size: 15px; color: var(--ink);
    font-family: Arial, sans-serif;
  }
</style>
</head>
<body>
<div class="site">
  <header>
    <div class="brand"><span class="brand-mark"></span>Vexor Ridge</div>
    <nav class="main-nav">
      <a class="is-active" href="#">Home</a>
      <a href="#">About</a>
      <a href="#">Services</a>
      <a href="#">Media</a>
      <a href="#">Contact</a>
    </nav>
    <div class="social">
      <span><i style="background:var(--social-a)"></i>chatterbay</span>
      <span><i style="background:var(--social-b)"></i>circlenet</span>
      <span><i style="background:var(--social-c)"></i>chirpline</span>
    </div>
  </header>

  <section class="tab" style="top:123px;">
    <div class="tab-head"><svg width="6" height="8"><path d="M0 0 L6 4 L0 8Z" fill="#888"/></svg>Banner 1 (Can add a slider here)</div>
  </section>
  <section class="tab" style="top:171px;">
    <div class="tab-head"><svg width="6" height="8"><path d="M0 0 L6 4 L0 8Z" fill="#888"/></svg>Banner 2</div>
  </section>
  <section class="tab" style="top:218px;">
    <div class="tab-head"><svg width="6" height="8"><path d="M0 0 L6 4 L0 8Z" fill="#888"/></svg>Banner 3</div>
  </section>
  <section class="tab is-open" style="top:266px;">
    <div class="tab-head"><svg width="8" height="6"><path d="M0 0 L8 0 L4 5Z" fill="#222"/></svg>Contact Form</div>
    <form class="contact-form">
      <label class="field-label" style="top:24px;">Name</label>
      <div class="field" style="top:28px;">Dara Vell</div>
      <label class="field-label" style="top:71px;">Email</label>
      <div class="field" style="top:75px;">dara@mailbox.example</div>
      <label class="field-label" style="top:118px;">Query</label>
      <div class="field is-area" style="top:122px;"></div>
      <button class="submit" type="button">Submit</button>
    </form>
  </section>

  <footer class="site-footer">Vexor Ridge © 2013</footer>
</div>
</body>
</html>
```